Business Card Design for Fashion Tech Startup

Dear designers, we need a business card for Asia's premier fashion tech startup.!

PebbleNest is discovery e-commerce destination for busy, discerning parents in Asia featuring leading independent designers of baby, kids fashion apparel and sustainable brands from around the world.

PebbleNest is a modern, contemporary fashion tech startup targeting well-educated, well travelled and affluent parents. We're NOT your typical kiddy store!! Our design philosophy & e-commerce site is more like Vorn.com, Quenibo.com, Darwick.com, Tamsfield.com.
Updates

Hi, size of the business card should be 84mm X 55mm. Would appreciate some business card layouts in Portrait as added consideration, i fancy the idea of a Portrait business card. What's important is that the business card should pique the receiver's interest to log onto the website to learn more. Many thanks and love forward to the designs!

Target Market(s)

Though modern, classy in look, feel & positioning, PebbleNest does possess a cheeky, fun-loving personality as depicted by its logo and the segment it targets (baby, kids) though the key decision makers i.e primarily mums between 25-40 who are well educated/travelled, local & expatriates, internet/digitally savvy, mid-high income working mums.

Industry/Entity Type

E-Commerce

Requirements
Must have
• Name, designation, email, phone & mobile number.
Company url : www.pebblenest.sg
Slogan : Discovery e-commerce destination for discerning, busy parents
Nice to have
• Call to Action such as a Discount code offering 10% discount
or asking people to "Like" us on our Facebook page/Facebook URL

```html
<!DOCTYPE html>
<html lang="en">
<head>
<meta charset="utf-8">
<title>PebbleNest Business Card</title>
<link href="https://fonts.googleapis.com/css2?family=Source+Sans+3:wght@400;600&display=swap" rel="stylesheet">
<style>
  :root {
    --page: #ffffff;
    --ink: #1c1c1c;
    --name-blue: #2458e4;
    --brand-green: #2f6650;
    --orange: #f7821e;
    --green: #6cbb1f;
    --rose: #ee3f6a;
    --sky: #3aa6ec;
    --violet: #c72ce0;
    --panel: rgba(255, 255, 255, 0.78);
  }
  * { margin: 0; padding: 0; box-sizing: border-box; }
  html, body {
    width: 1200px; height: 1019px; overflow: hidden;
    background: var(--page);
    font-family: "Source Sans 3", sans-serif;
    color: var(--ink);
  }
  .canvas { position: relative; width: 1200px; height: 1019px; }
  .card {
    position: absolute; top: 40px; width: 531px; height: 883px; overflow: hidden;
  }
  .card--front { left: 41px; }
  .card--back { left: 604px; }
  .burst {
    position: absolute; inset: 0;
    background:
      radial-gradient(circle at 50% 50%, rgba(255,255,255,1) 0%, rgba(255,255,255,0.9) 14%, rgba(255,255,255,0.35) 34%, rgba(255,255,255,0) 58%),
      conic-gradient(from 0deg at 50% 50%, #e7f21c 0deg, #a6d81b 45deg, #6dc9c8 95deg, #4b6ef0 135deg, #3b2fe0 160deg, #c122df 200deg, #ef2ec6 225deg, #f5318a 255deg, #f8452a 285deg, #fb8a1c 320deg, #e7f21c 360deg);
  }
  .card--back .burst {
    background:
      radial-gradient(circle at 50% 48%, rgba(255,255,255,0.85) 0%, rgba(255,255,255,0.3) 40%, rgba(255,255,255,0) 65%),
      conic-gradient(from 0deg at 50% 48%, #e5d018 0deg, #b3c41a 45deg, #61c9e8 95deg, #8a5de8 135deg, #6b2fd8 160deg, #b526d8 200deg, #e32fc8 225deg, #f03a6c 255deg, #f53a26 285deg, #fb8a1c 320deg, #e5d018 360deg);
  }
  .brand {
    position: absolute; left: 0; right: 0; text-align: center;
    font-weight: 600; color: var(--brand-green); letter-spacing: 0.5px; line-height: 1;
  }
  .brand-dot {
    position: absolute; border-radius: 50%; background: var(--brand-green);
  }
  .card--front .brand-dot { left: 190px; top: 260px; width: 150px; height: 150px; }
  .card--front .brand { top: 475px; font-size: 66px; }
  .slogan {
    position: absolute; left: 70px; right: 70px; top: 560px; text-align: center;
    font-size: 22px; line-height: 1.3; color: var(--brand-green); font-weight: 400;
  }
  .panel {
    position: absolute; left: 60px; top: 60px; width: 411px; height: 764px;
    background: var(--panel);
  }
  .panel .brand-dot { left: 138px; top: 22px; width: 135px; height: 135px; }
  .panel .brand { top: 208px; font-size: 54px; }
  .person { position: absolute; top: 330px; left: 0; right: 0; text-align: center; }
  .person-name { font-size: 52px; font-weight: 400; color: var(--name-blue); line-height: 1; }
  .person-role { font-size: 25px; margin-top: 14px; line-height: 1; }
  .contacts { position: absolute; left: 24px; top: 488px; list-style: none; }
  .contact { display: flex; align-items: center; height: 50px; font-size: 27px; white-space: nowrap; }
  .contact svg { width: 32px; height: 32px; margin-right: 14px; flex: none; }
  .side-label {
    position: absolute; top: 946px; width: 531px; text-align: center;
    font-size: 25px; letter-spacing: 0.5px;
  }
  .side-label--front { left: 41px; }
  .side-label--back { left: 604px; }
</style>
</head>
<body>
<div class="canvas">
  <section class="card card--front">
    <div class="burst" role="img" aria-label="Radiant rainbow light-burst background"></div>
    <div class="brand-dot"></div>
    <div class="brand">PebbleNest</div>
    <p class="slogan">Discovery e-commerce destination for discerning, busy parents</p>
  </section>

  <section class="card card--back">
    <div class="burst" role="img" aria-label="Radiant rainbow light-burst background"></div>
    <div class="panel">
      <div class="brand-dot"></div>
      <div class="brand">PebbleNest</div>
      <div class="person">
        <div class="person-name">Mara Lindqvist</div>
        <div class="person-role">Managing Director</div>
      </div>
      <ul class="contacts">
        <li class="contact">
          <svg viewBox="0 0 32 32"><circle cx="16" cy="16" r="16" fill="var(--orange)"/><path d="M9 16l7-6 7 6M11 15v7h4v-4h2v4h4v-7" fill="none" stroke="#fff" stroke-width="1.8" stroke-linejoin="round"/></svg>
          4120 Fenwick Row, QT 58204
        </li>
        <li class="contact">
          <svg viewBox="0 0 32 32"><circle cx="16" cy="16" r="16" fill="var(--green)"/><ellipse cx="16" cy="15" rx="7" ry="5.5" fill="none" stroke="#fff" stroke-width="1.8"/><path d="M12 19l-2 4 5-3" fill="none" stroke="#fff" stroke-width="1.8" stroke-linejoin="round"/></svg>
          555-014-2768
        </li>
        <li class="contact">
          <svg viewBox="0 0 32 32"><circle cx="16" cy="16" r="16" fill="var(--rose)"/><rect x="11" y="8" width="10" height="16" rx="2" fill="none" stroke="#fff" stroke-width="1.8"/><path d="M14.5 21h3" stroke="#fff" stroke-width="1.6"/></svg>
          555-019-4432
        </li>
        <li class="contact">
          <svg viewBox="0 0 32 32"><circle cx="16" cy="16" r="16" fill="var(--sky)"/><rect x="9" y="11" width="14" height="10" fill="none" stroke="#fff" stroke-width="1.8"/><path d="M9 11l7 6 7-6" fill="none" stroke="#fff" stroke-width="1.8"/></svg>
          mara@pebblenest.sg
        </li>
        <li class="contact">
          <svg viewBox="0 0 32 32"><circle cx="16" cy="16" r="16" fill="var(--violet)"/><rect x="9" y="10" width="14" height="12" fill="none" stroke="#fff" stroke-width="1.8"/><path d="M9 14h14M13 17h2M17 17h2M13 20h2M17 20h2" stroke="#fff" stroke-width="1.5"/></svg>
          www.pebblenest.sg
        </li>
      </ul>
    </div>
  </section>

  <div class="side-label side-label--front">FRONT SIDE</div>
  <div class="side-label side-label--back">BACK SIDE</div>
</div>
</body>
</html>
```